Email Signiture and letterhead design

we are looking for a modern business design to incorporate our logo and iso certification plus social icons for Twitter, LinkedIn, and youtube
they must include our UK vat and also company registration as text but I can fill these out. Email signature to have a link/icon to our webshop www.dremlox.co.uk

Target Market(s)

All

Font styles to use
Serif
Sans Serif

Requirements
Must have
• Address, tel, email , web details incorperated
Nice to have
• a professional looking letter head and email signiture, Email signature to have a link/icon to our webshop www.dremlox.co.uk

```html
<!DOCTYPE html>
<html lang="en">
<head>
<meta charset="utf-8">
<title>Dremlox Hubs &amp; Bearings Ltd – Letterhead and Email Signature</title>
<link rel="stylesheet" href="https://fonts.googleapis.com/css2?family=Poppins:wght@400;500;600&display=swap">
<style>
  :root{
    --brand-red:#ec1c24;
    --charcoal:#3d3d3f;
    --paper:#ffffff;
    --backdrop:#ec1c24;
    --photo-light:#9a9a9c;
    --photo-dark:#3a3a3c;
  }
  *{box-sizing:border-box;margin:0;padding:0}
  html,body{width:1200px;height:1200px;overflow:hidden}
  body{background:var(--backdrop);position:relative;font-family:"Poppins",sans-serif;color:var(--charcoal)}

  /* Letterhead */
  .letterhead{position:absolute;left:302px;top:81px;width:595px;height:841px;background:var(--paper);overflow:hidden}
  .letterhead-art{position:absolute;inset:0}
  .brand{display:flex;align-items:center;gap:9px;white-space:nowrap}
  .brand-mark{width:22px;height:22px;border-radius:50%;background:var(--brand-red);flex:none}
  .brand-name{font-weight:600;color:var(--charcoal);letter-spacing:.2px}
  .letterhead .brand{position:absolute;left:0;right:0;top:58px;justify-content:center}
  .letterhead .brand-name{font-size:20px}

  .contact-list{position:absolute;left:23px;top:740px;list-style:none}
  .contact-item{display:flex;align-items:center;height:21px;margin-bottom:1.5px;font-size:8.6px;letter-spacing:.5px}
  .contact-item .icon{width:19px;height:19px;flex:none;margin-right:6px}
  .contact-item.phone{color:var(--brand-red)}
  .contact-item.web{color:#fff;margin-top:1px}
  .contact-item.address{color:#fff;margin-top:3px}

  .social{position:absolute;left:447px;top:812px;display:flex;gap:6px}
  .social-badge{width:12px;height:12px;border:1px solid #fff}

  /* Email signature */
  .signature{position:absolute;left:206px;top:966px;width:789px;height:181px;background:var(--paper);overflow:hidden}
  .signature-art{position:absolute;inset:0}
  .signature .brand{position:absolute;left:46px;top:76px}
  .signature .brand-name{font-size:15px}
  .signature .brand-mark{width:18px;height:18px}

  .person{position:absolute;right:257px;top:22px;text-align:right}
  .person-name{font-size:19px;font-weight:600;line-height:1.1;color:var(--charcoal)}
  .person-role{font-size:11px;color:var(--brand-red);line-height:1.1}
  .name-square{position:absolute;left:539px;top:30px;width:22px;height:22px;background:var(--brand-red)}

  .sig-line{position:absolute;right:257px;font-size:10px;letter-spacing:.8px;white-space:nowrap}
  .sig-phone{top:94px}
  .sig-email{top:109px}
  .sig-web{top:134px;color:#fff}
  .sig-address{top:161px;color:#fff}

  .portrait{position:absolute;left:611px;top:34px;width:112px;height:112px;border-radius:50%;border:4px solid var(--brand-red);background:var(--paper);padding:3px}
  .portrait-photo{width:100%;height:100%;border-radius:50%;background:radial-gradient(circle at 50% 40%,var(--photo-light),var(--photo-dark))}
</style>
</head>
<body>

<section class="letterhead" aria-label="Letterhead">
  <svg class="letterhead-art" viewBox="0 0 595 841" aria-hidden="true">
    <line x1="32" y1="728" x2="32" y2="841" stroke="var(--brand-red)" stroke-width="1.2"/>
    <rect x="0" y="785" width="520" height="21" fill="var(--brand-red)"/>
    <rect x="0" y="812" width="515" height="21" fill="var(--charcoal)"/>
    <path d="M595,700 C530,725 500,780 494,841 L595,841Z" fill="var(--brand-red)"/>
    <path d="M595,713 C545,740 515,785 512,841 L595,841Z" fill="var(--charcoal)"/>
    <path d="M595,730 C555,755 530,795 530,841 L595,841Z" fill="var(--paper)"/>
  </svg>

  <div class="brand">
    <span class="brand-mark"></span>
    <span class="brand-name">Dremlox Hubs &amp; Bearings Ltd</span>
  </div>

  <ul class="contact-list">
    <li class="contact-item phone">
      <svg class="icon" viewBox="0 0 20 20" aria-hidden="true"><circle cx="10" cy="10" r="9" fill="#fff" stroke="var(--brand-red)" stroke-width="1.4"/><path d="M7,5.5 l2,2 -1,1.3 c.6,1.4 1.6,2.4 3,3 l1.3-1 2,2 -1.2,1.4 C9.5,14 6,10.5 5.6,6.7Z" fill="var(--brand-red)"/></svg>
      012-123-1234
    </li>
    <li class="contact-item email">
      <svg class="icon" viewBox="0 0 20 20" aria-hidden="true"><circle cx="10" cy="10" r="9" fill="#fff" stroke="var(--charcoal)" stroke-width="1.4"/><rect x="5.5" y="7" width="9" height="6.5" fill="none" stroke="var(--charcoal)" stroke-width="1"/><path d="M5.5,7 L10,10.8 14.5,7" fill="none" stroke="var(--charcoal)" stroke-width="1"/></svg>
      yourmailid@dremlox.co.uk
    </li>
    <li class="contact-item web">
      <svg class="icon" viewBox="0 0 20 20" aria-hidden="true"><circle cx="10" cy="10" r="9" fill="var(--brand-red)" stroke="#fff" stroke-width="1.4"/><g fill="none" stroke="#fff" stroke-width=".8"><circle cx="10" cy="10" r="4.5"/><ellipse cx="10" cy="10" rx="2" ry="4.5"/><line x1="5.5" y1="10" x2="14.5" y2="10"/></g></svg>
      www.dremlox.co.uk
    </li>
    <li class="contact-item address">
      <svg class="icon" viewBox="0 0 20 20" aria-hidden="true"><circle cx="10" cy="10" r="9" fill="var(--charcoal)" stroke="#fff" stroke-width="1.4"/><path d="M10,15 C7.5,11.5 6.8,10 6.8,8.6 a3.2,3.2 0 0 1 6.4,0 C13.2,10 12.5,11.5 10,15Z" fill="#fff"/><circle cx="10" cy="8.6" r="1.2" fill="var(--charcoal)"/></svg>
      your address, country name, city
    </li>
  </ul>

  <div class="social" aria-label="Social links">
    <span class="social-badge"></span><span class="social-badge"></span><span class="social-badge"></span>
  </div>
</section>

<section class="signature" aria-label="Email signature">
  <svg class="signature-art" viewBox="0 0 789 181" aria-hidden="true">
    <rect x="0" y="129" width="630" height="26" fill="var(--brand-red)"/>
    <rect x="0" y="155" width="620" height="26" fill="var(--charcoal)"/>
    <line x1="550" y1="86" x2="550" y2="181" stroke="var(--brand-red)" stroke-width="1.2"/>
    <path d="M789,0 L760,0 C690,20 625,90 614,181 L789,181Z" fill="var(--brand-red)"/>
    <path d="M789,0 C715,25 650,100 638,181 L789,181Z" fill="var(--charcoal)"/>
    <path d="M789,8 C725,40 670,110 660,181 L789,181Z" fill="var(--paper)"/>
    <circle cx="550" cy="142" r="11.5" fill="var(--brand-red)" stroke="#fff" stroke-width="1.4"/>
    <g fill="none" stroke="#fff" stroke-width=".8"><circle cx="550" cy="142" r="6"/><ellipse cx="550" cy="142" rx="2.6" ry="6"/><line x1="544" y1="142" x2="556" y2="142"/></g>
  </svg>

  <div class="brand">
    <span class="brand-mark"></span>
    <span class="brand-name">Dremlox Hubs &amp; Bearings Ltd</span>
  </div>

  <div class="person">
    <div class="person-name">Your Name</div>
    <div class="person-role">Designation</div>
  </div>
  <span class="name-square"></span>

  <div class="sig-line sig-phone">012-123-1234</div>
  <div class="sig-line sig-email">yourmailid@dremlox.co.uk</div>
  <div class="sig-line sig-web">yourwebsitename.com</div>
  <div class="sig-line sig-address">your address, country name, city</div>

  <div class="portrait">
    <div class="portrait-photo" role="img" aria-label="Portrait photo of the sender"></div>
  </div>
</section>

</body>
</html>
```